Fahrzeugbeschriftung für Unternehmen im Bereich der Glasfaser-Montage
Zielgruppe
Wir sind im Bereich der Glasfaser-Montage tätig,
einblasen von Glasfaser Kabel, herstellen von LWL Splicen
Tätigkeitsstichworte:
LWL Einblasarbeiten
LWL Splicearbeiten
Entstörungsservice
Druckprüfunge Flowkarohre
Aufgabenstellung
Die Beschriftung muss sich an der vorhandenen KFZ Beschriftung der Wendt Elektro GmbH orientieren, da
wir uns mit dieser Firmen zusammen schließen werden.

```html
<!DOCTYPE html>
<html lang="de">
<head>
<meta charset="utf-8">
<title>Wendt Elektro – Fahrzeugbeschriftung</title>
<link href="https://fonts.googleapis.com/css2?family=Archivo+Black&family=Arimo:wght@700&display=swap" rel="stylesheet">
<style>
  :root {
    --page: #e9eaeb;
    --panel: #fbfbfa;
    --panel-edge: #d6d7d8;
    --brand-green: #12a57f;
    --band: #a3a3a3;
    --ink: #1e1e1e;
    --photo-a: #c9b8ab;
    --photo-b: #e79a9c;
    --photo-c: #7d7a72;
  }
  * { margin: 0; padding: 0; box-sizing: border-box; }
  html, body { width: 1200px; height: 1176px; overflow: hidden; background: var(--page); }
  .wrap-layout { display: block; width: 1200px; height: 588px; }
  .body-panel { fill: var(--panel); stroke: var(--panel-edge); stroke-width: 2; }
  .photo-area { fill: url(#photoTone); }
  .info-band { fill: var(--band); opacity: 0.85; }
  .band-text { font-family: "Arimo", Arial, sans-serif; font-weight: 700; font-size: 15px; fill: var(--ink); letter-spacing: 0.3px; }
  .brand-name { font-family: "Archivo Black", "Arial Black", sans-serif; fill: var(--brand-green); }
  .brand-name--driver { font-size: 58px; }
  .brand-name--passenger { font-size: 50px; }
  .service-list { font-family: "Arimo", Arial, sans-serif; font-weight: 700; font-size: 14px; fill: var(--ink); }
</style>
</head>
<body>
<svg width="0" height="0" style="position:absolute">
  <defs>
    <linearGradient id="photoTone" x1="0" y1="0" x2="1" y2="1">
      <stop offset="0" stop-color="#7d7a72"/>
      <stop offset="0.45" stop-color="#c9b8ab"/>
      <stop offset="1" stop-color="#e79a9c"/>
    </linearGradient>
  </defs>
</svg>

<!-- Fahrerseite -->
<svg class="wrap-layout driver-side" viewBox="0 0 1200 588">
  <rect class="body-panel" x="50" y="92" width="1100" height="372" rx="40"/>
  <polygon class="photo-area" points="550,93 921,93 921,127 550,272" role="img" aria-label="Foto: Hand führt rosa Glasfaser-Leerrohre in einen Schacht"/>
  <g transform="translate(587,452) rotate(-19.4)">
    <text class="brand-name brand-name--driver" x="14" y="-34">Wendt Elektro</text>
    <rect class="info-band" x="0" y="-22" width="588" height="30"/>
    <text class="band-text" x="24" y="-2">78999 Seeburg   •   Tel. 07700 - 4821   •   www.wendt-elektro.de</text>
  </g>
  <text class="service-list" x="314" y="325">
    <tspan x="314" dy="0">LWL Einblasarbeiten</tspan>
    <tspan x="314" dy="16">LWL Splicearbeiten</tspan>
    <tspan x="314" dy="16">Entstörungsservice</tspan>
    <tspan x="314" dy="16">Druckprüfunge Flowkarohre</tspan>
  </text>
</svg>

<!-- Beifahrerseite -->
<svg class="wrap-layout passenger-side" viewBox="0 0 1200 588">
  <rect class="body-panel" x="50" y="72" width="1100" height="380" rx="40"/>
  <polygon class="photo-area" points="307,80 674,80 674,105 307,249" role="img" aria-label="Foto: Hand führt rosa Glasfaser-Leerrohre in einen Schacht"/>
  <g transform="translate(328,425) rotate(-21)">
    <text class="brand-name brand-name--passenger" x="10" y="-32">Wendt Elektro</text>
    <rect class="info-band" x="0" y="-22" width="530" height="30"/>
    <text class="band-text" x="16" y="-2">78999 Seeburg   •   Tel. 07700 - 4821   •   www.wendt-elektro.de</text>
  </g>
  <text class="service-list" x="690" y="320">
    <tspan x="690" dy="0">LWL Einblasarbeiten</tspan>
    <tspan x="690" dy="16">LWL Splicearbeiten</tspan>
    <tspan x="690" dy="16">Entstörungsservice</tspan>
    <tspan x="690" dy="16">Druckprüfunge Flowkarohre</tspan>
  </text>
</svg>
</body>
</html>
```